Franchise Vacation Rental Company Website

We are looking for fresh, new and creative design ideas to help enhance this site. We are a vacation rental company that is starting a new franchise business. This will be our home franchise page, and will need to appeal to franchise candidates as well as travelers looking for vacation homes in our current locations.

Business

```html
<!DOCTYPE html>
<html lang="en">
<head>
<meta charset="utf-8">
<title>BayHaven – Vacation Rental Services</title>
<link rel="stylesheet" href="https://fonts.googleapis.com/css2?family=Lato:wght@300;400&display=swap">
<style>
  :root {
    --green: #86c232;
    --green-dark: #6a9c22;
    --room: #e6e6e6;
    --room-wall: #d9d9d9;
    --room-edge: #bcbcbc;
    --hero-tone: #4a97cf;
    --rentals-tone: #4d6f92;
    --tile-tone: #7d8c93;
    --text: #333333;
    --muted: #8a8a8a;
    --footer: #222222;
    --footer-text: #8d8d8d;
    --footer-head: #bdbdbd;
    --social: #3d3d3d;
    --black: #0d0d0d;
    --white: #ffffff;
  }
  * { box-sizing: border-box; margin: 0; padding: 0; }
  html, body { width: 777px; height: 1200px; overflow: hidden; }
  body { position: relative; background: var(--white); font-family: "Lato", "Calibri", sans-serif; font-weight: 400; color: var(--text); }
  .abs { position: absolute; }

  /* header / room */
  .stage { left: 0; top: 0; width: 777px; height: 308px; background: var(--room); }
  .stage svg { position: absolute; left: 0; top: 0; }
  .brand { left: 170px; top: 16px; font-size: 19px; color: var(--green); }
  .nav { left: 268px; top: 19px; display: flex; font-size: 8px; color: var(--muted); }
  .nav a { color: inherit; text-decoration: none; height: 17px; line-height: 17px; margin-right: 18px; }
  .nav a.active { background: var(--green); color: var(--white); padding: 0 11px; position: relative; margin-right: 15px; }
  .nav a.active::after { content: ""; position: absolute; left: 50%; bottom: -4px; margin-left: -4px; border: 4px solid transparent; border-bottom: 0; border-top-color: var(--green); }
  .hero { left: 147px; top: 56px; width: 488px; height: 194px; background: var(--hero-tone); border: 2px solid var(--white); }
  .hero-title { left: 430px; top: 126px; background: var(--green); color: var(--white); font-size: 29px; line-height: 28px; padding: 0 3px; }
  .hero-sub { left: 434px; top: 156px; font-size: 13px; color: #111; }

  /* rentals */
  .rentals { left: 0; top: 308px; width: 777px; height: 383px; background: var(--rentals-tone); }
  .search-title { left: 169px; top: 366px; font-size: 18px; font-weight: 400; color: var(--white); }
  .field { left: 161px; width: 127px; height: 21px; border: 1px solid rgba(255,255,255,0.45); color: var(--white); font-size: 8px; line-height: 19px; padding-left: 8px; }
  .search-btn { left: 161px; top: 449px; width: 127px; height: 21px; background: var(--green); color: var(--white); font-size: 8.5px; line-height: 21px; text-align: center; }
  .tile { width: 156px; height: 129px; background: var(--tile-tone); }
  .tile-label { width: 142px; height: 29px; background: var(--black); color: var(--white); font-size: 9px; line-height: 29px; text-align: center; }

  /* signup */
  .signup { left: 146px; top: 671px; width: 486px; height: 55px; background: var(--white); border: 1px solid #eeeeee; box-shadow: 0 10px 8px -8px rgba(0,0,0,0.25); }
  .signup-text { left: 172px; top: 691px; font-size: 10.5px; color: #555; }
  .email { left: 341px; top: 687px; width: 172px; height: 23px; background: #f1f1f1; border: 1px solid #e2e2e2; font-size: 7px; color: #999; line-height: 21px; padding-left: 11px; }
  .submit { left: 524px; top: 687px; width: 83px; height: 23px; background: var(--green); color: var(--white); font-size: 8px; line-height: 23px; text-align: center; }

  /* features */
  .feature { width: 150px; text-align: center; }
  .feature h3 { font-weight: 400; font-size: 10.5px; color: #222; height: 18px; }
  .feature svg { display: block; margin: 12px auto 0; }
  .feature p { margin-top: 16px; font-size: 6.5px; line-height: 8px; color: #444; }

  /* footer */
  .footer { left: 0; top: 968px; width: 777px; height: 232px; background: var(--footer); }
  .foot-head { top: 1017px; font-size: 12px; font-weight: 300; color: var(--footer-head); }
  .foot-links { left: 146px; top: 1043px; list-style: none; font-size: 8px; font-weight: 300; color: var(--footer-text); line-height: 14.7px; }
  .contact { left: 331px; font-size: 8px; color: var(--footer-text); display: flex; align-items: center; gap: 7px; }
  .social { top: 1045px; width: 23px; height: 23px; background: var(--social); border: 1px solid #4a4a4a; }
  .rule { left: 0; top: 1159px; width: 777px; height: 1px; background: #3a3a3a; }
  .copyright { left: 0; top: 1179px; width: 777px; text-align: center; font-size: 6.5px; color: var(--footer-text); }
</style>
</head>
<body>

<section class="abs stage">
  <svg width="777" height="308" viewBox="0 0 777 308" aria-hidden="true">
    <polygon points="0,0 145,0 145,250 0,300" fill="var(--room-wall)"/>
    <polygon points="777,0 637,0 637,250 777,300" fill="var(--room-wall)"/>
    <line x1="145" y1="250" x2="0" y2="300" stroke="var(--room-edge)" stroke-width="2"/>
    <line x1="637" y1="250" x2="777" y2="300" stroke="var(--room-edge)" stroke-width="2"/>
  </svg>
  <div class="abs brand">BayHaven</div>
  <nav class="abs nav">
    <a class="active">Home</a><a>Spots</a><a>Franchise</a><a>List Properties</a><a>Rentals</a><a>News</a><a>Contact</a>
  </nav>
</section>
<div class="abs hero" role="img" aria-label="Photo of a traveller looking out over a calm sunlit sea"></div>
<div class="abs hero-title">Vacation</div>
<div class="abs hero-sub">Rental Services</div>

<section class="abs rentals" role="img" aria-label="Blurred coastal backdrop photo"></section>
<h2 class="abs search-title">Search Rentals</h2>
<div class="abs field" style="top:399px">Destination</div>
<div class="abs field" style="top:423px">Room</div>
<div class="abs search-btn">Search</div>

<div class="abs tile" style="left:312px;top:350px" role="img" aria-label="Photo of sailboats moored at a dock"></div>
<div class="abs tile" style="left:477px;top:350px" role="img" aria-label="Photo of a tidal island with a castle"></div>
<div class="abs tile" style="left:147px;top:504px" role="img" aria-label="Photo of a marina with boats and houses"></div>
<div class="abs tile" style="left:312px;top:504px" role="img" aria-label="Photo of a tidal island with a castle"></div>
<div class="abs tile" style="left:477px;top:504px" role="img" aria-label="Photo of a marina with boats and houses"></div>

<div class="abs tile-label" style="left:319px;top:465px">Maryland Eastern Shore</div>
<div class="abs tile-label" style="left:484px;top:465px">Maryland Eastern Shore</div>
<div class="abs tile-label" style="left:154px;top:619px">Maryland Eastern Shore</div>
<div class="abs tile-label" style="left:319px;top:619px">Maryland Eastern Shore</div>
<div class="abs tile-label" style="left:484px;top:619px">Maryland Eastern Shore</div>

<div class="abs signup"></div>
<div class="abs signup-text">Signup for last getaway deals</div>
<div class="abs email">Enter Your email</div>
<div class="abs submit">Submit</div>

<div class="abs feature" style="left:151px;top:775px">
  <h3>Great Spot</h3>
  <svg width="60" height="84" viewBox="0 0 60 84" aria-hidden="true">
    <circle cx="30" cy="29" r="28" fill="var(--green)"/>
    <path d="M30 20a6.5 6.5 0 0 0-6.5 6.5c0 5 6.5 11.5 6.5 11.5s6.5-6.5 6.5-11.5A6.5 6.5 0 0 0 30 20z" fill="#fff"/>
    <circle cx="30" cy="26.5" r="2.4" fill="var(--green)"/>
    <line x1="30" y1="57" x2="30" y2="80" stroke="var(--green-dark)"/>
    <path d="M27.5 78l2.5 4 2.5-4z" fill="var(--green-dark)"/>
  </svg>
  <p>Lorem ipsum dolor sit<br>amet this is a dummy texts lorem<br>ipsum dolor sit amet</p>
</div>
<div class="abs feature" style="left:307px;top:775px">
  <h3>Spot Travels free</h3>
  <svg width="60" height="84" viewBox="0 0 60 84" aria-hidden="true">
    <circle cx="30" cy="29" r="28" fill="var(--green)"/>
    <ellipse cx="29" cy="31" rx="3.6" ry="6.5" fill="#fff"/>
    <circle cx="27" cy="39.5" r="2.6" fill="#fff"/>
    <circle cx="27.5" cy="21.5" r="1.6" fill="#fff"/>
    <circle cx="30.5" cy="21" r="1.3" fill="#fff"/>
    <circle cx="33" cy="22" r="1.1" fill="#fff"/>
    <line x1="30" y1="57" x2="30" y2="80" stroke="var(--green-dark)"/>
    <path d="M27.5 78l2.5 4 2.5-4z" fill="var(--green-dark)"/>
  </svg>
  <p>Lorem ipsum dolor sit<br>amet this is a dummy texts lorem<br>ipsum dolor sit amet</p>
</div>
<div class="abs feature" style="left:467px;top:775px">
  <h3>Last Min Deads</h3>
  <svg width="60" height="84" viewBox="0 0 60 84" aria-hidden="true">
    <circle cx="30" cy="29" r="28" fill="var(--green)"/>
    <circle cx="30" cy="29" r="8" fill="none" stroke="#fff" stroke-width="1.4"/>
    <path d="M30 24v5h-4" fill="none" stroke="#fff" stroke-width="1.4"/>
    <line x1="30" y1="57" x2="30" y2="80" stroke="var(--green-dark)"/>
    <path d="M27.5 78l2.5 4 2.5-4z" fill="var(--green-dark)"/>
  </svg>
  <p>Lorem ipsum dolor sit<br>amet this is a dummy texts lorem<br>ipsum dolor sit amet</p>
</div>

<footer class="abs footer"></footer>
<h4 class="abs foot-head" style="left:146px">Know More About US</h4>
<ul class="abs foot-links">
  <li>Who we are?</li><li>What we do?</li><li>Franchise Information</li><li>Our Philosophy</li>
</ul>
<h4 class="abs foot-head" style="left:331px">Contact Us</h4>
<div class="abs contact" style="top:1044px">
  <svg width="10" height="10" viewBox="0 0 10 10" aria-hidden="true"><path d="M2 0.5l2 2-1 1.3c.6 1.3 1.8 2.5 3.2 3.2l1.3-1 2 2-1.3 1.5C4.5 9.5.5 5.5.5 1.8z" fill="#9a9a9a"/></svg>
  <span>+1 555 014 2290</span>
</div>
<div class="abs contact" style="top:1065px">
  <svg width="10" height="8" viewBox="0 0 10 8" aria-hidden="true"><rect width="10" height="8" fill="#9a9a9a"/><path d="M0 0l5 4 5-4" fill="none" stroke="#222" stroke-width="1"/></svg>
  <span>hello@bayhaven-stays.com</span>
</div>
<h4 class="abs foot-head" style="left:498px">Find us on</h4>
<div class="abs social" style="left:498px" role="img" aria-label="Social network link"></div>
<div class="abs social" style="left:525px" role="img" aria-label="Social network link"></div>
<div class="abs social" style="left:552px" role="img" aria-label="Social network link"></div>
<div class="abs social" style="left:578px" role="img" aria-label="Social network link"></div>
<div class="abs social" style="left:605px" role="img" aria-label="Social network link"></div>
<div class="abs rule"></div>
<div class="abs copyright">Copyright text @ lorem ipsum.</div>

</body>
</html>
```